Refrigerator Banner

We are purchasing a container of refrigerators. One of our competitors overseas has a really nice sticker/canopy header on top of the light box. please see attched Pic A & Pic B.
Now, we would like to have a sort of similar look and just different enough not to upset anyone. However, this competitor is on the other side of the world, so we don't really compete with each other. So maybe the same blue but have the water thinghy a bit different.
Also, our brand name is "BROOKLINE Refrigeration"
I would design in the following dimensions:
• 572mm × 223mm
• 1125mm × 223mm
• 1705mm × 223mm
thanks

```html
<!DOCTYPE html>
<html lang="en">
<head>
<meta charset="utf-8">
<title>BROOKLINE Refrigeration – Canopy Header Banners</title>
<link rel="stylesheet" href="https://fonts.googleapis.com/css2?family=Tinos:wght@700&display=swap">
<style>
  :root {
    --page: #ffffff;
    --navy-deep: #04042a;
    --navy: #0c1850;
    --blue-mid: #1c4788;
    --blue-glow: #2d64a8;
    --water-core: rgba(225, 238, 255, 0.55);
    --water-haze: rgba(170, 205, 245, 0.22);
    --water-warm: rgba(225, 140, 130, 0.28);
    --type: #ffffff;
  }

  * { box-sizing: border-box; margin: 0; padding: 0; }

  html, body {
    width: 1200px;
    height: 900px;
    overflow: hidden;
    background: var(--page);
  }

  .sheet {
    position: relative;
    width: 1200px;
    height: 900px;
  }

  .banner {
    position: absolute;
    overflow: hidden;
    background:
      radial-gradient(ellipse 50% 90% at 50% 70%, var(--blue-glow) 0%, var(--blue-mid) 35%, var(--navy) 72%, var(--navy-deep) 100%);
  }

  .banner--small  { left: 237px; top: 57px;  width: 777px;  height: 302px; }
  .banner--medium { left: 128px; top: 395px; width: 968px;  height: 190px; }
  .banner--large  { left: 42px;  top: 651px; width: 1139px; height: 149px; }

  /* water splash: soft haze band with a thin bright streak through it */
  .water-splash {
    position: absolute;
    background:
      linear-gradient(90deg, var(--water-warm) 0%, var(--water-haze) 25%, var(--water-haze) 75%, var(--water-warm) 100%);
    -webkit-mask-image: radial-gradient(ellipse closest-side at 50% 50%, #000 20%, rgba(0,0,0,0.5) 55%, transparent 100%);
            mask-image: radial-gradient(ellipse closest-side at 50% 50%, #000 20%, rgba(0,0,0,0.5) 55%, transparent 100%);
    filter: blur(3px);
  }

  .water-splash::before {
    content: "";
    position: absolute;
    left: 4%;
    right: 4%;
    top: 46%;
    height: 8%;
    border-radius: 50%;
    background: linear-gradient(90deg, rgba(235, 160, 150, 0.6) 0%, var(--water-core) 30%, var(--water-core) 70%, rgba(235, 160, 150, 0.6) 100%);
    filter: blur(1.5px);
  }

  .banner--small .water-splash  { left: 0;     top: 84px; width: 775px; height: 90px; }
  .banner--medium .water-splash { left: 0;     top: 62px; width: 900px; height: 70px; }
  .banner--large .water-splash  { left: 150px; top: 36px; width: 740px; height: 56px; }

  .brand {
    position: absolute;
    display: inline-block;
    color: var(--type);
    font-family: "Tinos", "Times New Roman", serif;
    font-weight: 700;
    line-height: 1;
    text-align: right;
  }

  .brand__name {
    display: block;
    letter-spacing: 0.01em;
  }

  .brand__tagline {
    display: block;
    letter-spacing: 0.06em;
  }

  .banner--small .brand  { right: 30px; top: 236px; }
  .banner--small .brand__name    { font-size: 35px; }
  .banner--small .brand__tagline { font-size: 16px; margin-top: 2px; margin-right: -5px; }

  .banner--medium .brand { left: 370px; top: 90px; }
  .banner--medium .brand__name    { font-size: 40px; }
  .banner--medium .brand__tagline { font-size: 18px; margin-top: 1px; margin-right: -4px; }

  .banner--large .brand  { right: 21px; top: 88px; }
  .banner--large .brand__name    { font-size: 30px; }
  .banner--large .brand__tagline { font-size: 16px; margin-top: 1px; margin-right: -3px; }
</style>
</head>
<body>
  <main class="sheet">
    <section class="banner banner--small" aria-label="Canopy header, 572 by 223 mm">
      <div class="water-splash" role="img" aria-label="Photographic splash of clear water running across the banner"></div>
      <p class="brand">
        <span class="brand__name">BROOKLINE</span>
        <span class="brand__tagline">Refrigeration</span>
      </p>
    </section>

    <section class="banner banner--medium" aria-label="Canopy header, 1125 by 223 mm">
      <div class="water-splash" role="img" aria-label="Photographic splash of clear water running across the banner"></div>
      <p class="brand">
        <span class="brand__name">BROOKLINE</span>
        <span class="brand__tagline">Refrigeration</span>
      </p>
    </section>

    <section class="banner banner--large" aria-label="Canopy header, 1705 by 223 mm">
      <div class="water-splash" role="img" aria-label="Photographic splash of clear water running across the banner"></div>
      <p class="brand">
        <span class="brand__name">BROOKLINE</span>
        <span class="brand__tagline">Refrigeration</span>
      </p>
    </section>
  </main>
</body>
</html>
```